A6 Advertising Post Card

I am looking for refinement on this idea for an advertising letter-box drop of an A6 postcard.
Side 1 - our brand, the address, "15% discount if you present this card before Dec 31"

We are a new retail concept in terms of the store concept.

Side 2 - i want to highlight where the products are from, what materials are used, emphasis on cool, fresh, different, affordable, the product ranges grouped by colours (storage &organisation items in 1 colour or font, illumination products in 1 colour or font, furniture in 1 colour or font, decor in 1 colour or font, curios is 1 colour or font, fasion in 1 colour or font, others in a 1 colour or font)

The Product Categories:
see attachment

Hi

I've added the product categories with products sorted under each heading. I have also added the logo in a variety of file types (jpg, tif, psd, png). The sky blue background is part of the brand image.
Thanks

Target Market(s)

Home-makers (men and women) and women of all ages. Decision makers for home furnishings. Cross demographic - this is not premium..affordable to all social strata.
The brand is about fun, colourful and functional home stuff. The fashion stuff is a small percentage of the overall offer - targeting women who should spoil themselves as they spoil their families with nice stuff for the home.

Industry/Entity Type

Advertising

```html
<!DOCTYPE html>
<html lang="en">
<head>
<meta charset="utf-8">
<title>Kedai – A6 Postcard</title>
<link rel="stylesheet" href="https://fonts.googleapis.com/css2?family=Questrial&family=PT+Sans+Narrow:wght@400;700&family=Open+Sans:ital,wght@0,700;0,800;1,400&display=swap">
<style>
  :root {
    --sky: #1ff0ee;
    --violet: #6a1ef0;
    --deep-blue: #2a18c8;
    --plum: #5a1470;
    --ink: #1a1a1a;
    --white: #ffffff;
    --brand-red: #e8401c;
    --olive: #5f7a1e;
    --coral: #f26a3d;
    --sun: #fff200;
    --illumination: #a9cdf6;
    --storage: #f7941d;
    --curios: #c9c4f0;
    --furniture: #2f8ff0;
    --decor: #fff35a;
    --misc: #6b8e23;
    --fashion: #4b5b27;
  }
  * { box-sizing: border-box; margin: 0; padding: 0; }
  html, body { width: 1200px; height: 503px; overflow: hidden; background: var(--white); }
  .canvas { position: relative; width: 1200px; height: 503px; }

  /* ---------- Front ---------- */
  .front {
    position: absolute; left: 38px; top: 42px; width: 538px; height: 380px;
    background: var(--sky); overflow: hidden;
    box-shadow: 2px 3px 5px rgba(0,0,0,.35);
  }
  .front__waves { position: absolute; inset: 0; }
  .front__brand {
    position: absolute; left: 0; right: 0; top: 40px; text-align: center;
    font-family: "Questrial", sans-serif; font-size: 140px; line-height: 1;
    color: var(--brand-red); letter-spacing: 2px;
  }
  .front__tagline {
    position: absolute; left: 192px; top: 214px;
    font-family: "Questrial", sans-serif; font-size: 33px; color: var(--plum);
    display: flex; align-items: center; gap: 14px;
  }
  .front__tagline .diamond {
    width: 14px; height: 14px; background: #6e6e8a; transform: rotate(45deg);
    border: 1px solid #444;
  }
  .offer { position: absolute; left: 8px; top: 208px; width: 182px; height: 134px; }
  .offer__text {
    position: absolute; inset: 0; display: flex; align-items: center; justify-content: center;
    text-align: center; font-family: "Open Sans", sans-serif; font-weight: 800;
    font-size: 15.5px; line-height: 18px; color: var(--white);
  }
  .front__address {
    position: absolute; left: 0; right: 0; bottom: 12px; text-align: center;
    font-family: "Questrial", sans-serif; font-size: 21px; color: var(--white);
  }

  /* ---------- Back ---------- */
  .back {
    position: absolute; left: 618px; top: 84px; width: 540px; height: 382px;
    background: var(--sky); overflow: hidden;
    box-shadow: 2px 3px 5px rgba(0,0,0,.35);
  }
  .back__bg { position: absolute; inset: 0; }
  .back__headline {
    position: absolute; left: 28px; top: 24px;
    font-family: "Open Sans", sans-serif; font-weight: 700; font-size: 17px; color: var(--deep-blue);
  }
  .back__values {
    position: absolute; left: 28px; top: 52px;
    font-family: "Open Sans", sans-serif; font-weight: 700; font-size: 10px; color: var(--deep-blue);
  }
  .back__brand {
    position: absolute; right: 26px; top: 24px;
    font-family: "Questrial", sans-serif; font-size: 30px; color: var(--brand-red);
  }
  .back__origin {
    position: absolute; left: 28px; top: 88px;
    font-family: "Open Sans", sans-serif; font-style: italic; font-size: 11.5px; color: var(--deep-blue);
    transform: rotate(-1.2deg); transform-origin: left center; white-space: nowrap;
  }
  .product-photo { position: absolute; top: 106px; height: 78px; }
  .product-photo--basket { left: 0; width: 94px; background: linear-gradient(#9ab3a0, #8a5a3a); }
  .product-photo--drum { left: 102px; width: 88px; background: linear-gradient(90deg, #e8e8e8, #6b3a1c 50%, #e8e8e8); }
  .product-photo--vase { left: 198px; width: 92px; background: linear-gradient(#c9302c, #f3d6d0 55%, #b02a26); }
  .product-photo--plate { left: 298px; width: 136px; background: linear-gradient(135deg, #c8b07a, #4a5a8a 60%, #8a94b8); }
  .product-photo--jar { left: 442px; width: 98px; background: linear-gradient(90deg, #dfe8f2, #3a5aa8 50%, #dfe8f2); }

  .range {
    position: absolute; top: 204px; bottom: 0; padding: 6px 4px 0 16px;
    font-family: "PT Sans Narrow", sans-serif; font-size: 9.6px; line-height: 12.3px;
  }
  .range__title {
    position: absolute; left: 1px; top: 6px; writing-mode: vertical-rl; transform: rotate(180deg);
    font-family: "PT Sans Narrow", sans-serif; font-weight: 700; font-size: 11px; line-height: 13px;
    white-space: nowrap;
  }
  .range ul { list-style: none; }
  .range--illumination { left: 12px; width: 84px; background: linear-gradient(90deg, var(--violet) 14px, var(--illumination) 14px); color: var(--ink); }
  .range--illumination .range__title { color: var(--illumination); }
  .range--storage { left: 104px; width: 80px; background: linear-gradient(90deg, var(--violet) 14px, var(--storage) 14px); color: var(--white); }
  .range--storage .range__title { color: var(--storage); }
  .range--curios { left: 192px; width: 78px; background: linear-gradient(90deg, var(--violet) 14px, var(--curios) 14px); color: var(--ink); }
  .range--curios .range__title { color: var(--storage); }
  .range--furniture { left: 278px; width: 80px; background: linear-gradient(90deg, var(--violet) 14px, var(--furniture) 14px); color: var(--white); }
  .range--furniture .range__title { color: var(--furniture); }
  .range--decor { left: 364px; width: 84px; background: linear-gradient(90deg, var(--violet) 14px, var(--decor) 14px); color: var(--ink); }
  .range--decor .range__title { color: var(--storage); }
  .range--misc { left: 454px; width: 82px; top: 188px; bottom: 86px; background: linear-gradient(90deg, var(--deep-blue) 14px, var(--misc) 14px); color: var(--white); padding-top: 8px; }
  .range--misc .range__title { color: var(--misc); }
  .range--fashion { left: 454px; width: 82px; top: 302px; background: linear-gradient(90deg, var(--deep-blue) 14px, var(--fashion) 14px); color: var(--white); }
  .range--fashion .range__title { color: var(--misc); }
</style>
</head>
<body>
<main class="canvas">

  <section class="front" aria-label="Postcard front">
    <svg class="front__waves" width="538" height="380" viewBox="0 0 538 380" aria-hidden="true">
      <path d="M0 300 C120 330 300 300 538 300 L538 380 L0 380 Z" fill="var(--violet)"/>
      <path d="M20 318 C180 270 360 258 538 252" fill="none" stroke="var(--olive)" stroke-width="10"/>
      <path d="M20 324 C190 285 370 272 538 268" fill="none" stroke="var(--coral)" stroke-width="12"/>
      <path d="M20 330 C200 302 380 290 538 286" fill="none" stroke="var(--sun)" stroke-width="11"/>
      <path d="M20 336 C210 318 390 306 538 302" fill="none" stroke="var(--white)" stroke-width="6"/>
    </svg>
    <div class="front__brand">Kedai</div>
    <div class="front__tagline"><span>home</span><span class="diamond"></span><span>gifts</span></div>
    <div class="offer">
      <svg width="182" height="134" viewBox="0 0 182 134" aria-hidden="true">
        <g fill="#000" stroke="#bbb" stroke-width="3">
          <circle cx="50" cy="38" r="32"/><circle cx="100" cy="30" r="30"/><circle cx="142" cy="46" r="32"/>
          <circle cx="150" cy="92" r="30"/><circle cx="100" cy="106" r="28"/><circle cx="46" cy="98" r="32"/>
          <circle cx="30" cy="66" r="26"/>
        </g>
        <ellipse cx="91" cy="68" rx="80" ry="52" fill="#000"/>
      </svg>
      <p class="offer__text">15% Discount<br>- present card<br>before<br>Dec 31 2013</p>
    </div>
    <p class="front__address">A new store concept at 42 Market Lane, Eastwood</p>
  </section>

  <section class="back" aria-label="Postcard back">
    <svg class="back__bg" width="540" height="382" viewBox="0 0 540 382" aria-hidden="true">
      <path d="M0 190 C120 176 230 206 340 192 C420 182 480 196 540 186 L540 382 L0 382 Z" fill="var(--violet)"/>
      <path d="M0 372 L540 372 L540 382 L0 382 Z" fill="var(--deep-blue)"/>
      <path d="M0 100 C140 94 260 112 380 100 C450 94 500 98 540 92" fill="none" stroke="var(--deep-blue)" stroke-width="1.5"/>
    </svg>
    <h1 class="back__headline">A new store concept</h1>
    <p class="back__values">Fresh • Cool • Exotic • Modern</p>
    <p class="back__brand">Kedai</p>
    <p class="back__origin">Handmade from India • Philippines • Thailand • Indonesia • Malaysia • Nepal</p>

    <div class="product-photo product-photo--basket" role="img" aria-label="Photo of a woven basket"></div>
    <div class="product-photo product-photo--drum" role="img" aria-label="Photo of a carved hand drum"></div>
    <div class="product-photo product-photo--vase" role="img" aria-label="Photo of a red and white painted vase"></div>
    <div class="product-photo product-photo--plate" role="img" aria-label="Photo of a blue glass platter on leaves"></div>
    <div class="product-photo product-photo--jar" role="img" aria-label="Photo of a blue and white ceramic vase"></div>

    <div class="range range--illumination"><h2 class="range__title">Illumination</h2>
      <ul><li>Glass Votives</li><li>Lamps</li><li>Moroccan Lanterns</li><li>Chandeliers</li><li>Candle Holders</li><li>Candles</li><li>Tee-light Holders</li><li>Pendant Lights</li><li>Lantern Stands</li></ul></div>
    <div class="range range--storage"><h2 class="range__title">Storage &amp; Organisation</h2>
      <ul><li>Baskets</li><li>Trays</li><li>Drawers</li><li>Boxes</li><li>Tiffin Carrier</li><li>Plates</li><li>Bowls</li><li>Napkin Rings</li><li>Bamboo Towel Stands</li><li>Mugs</li><li>Cups</li><li>Water Jugs</li></ul></div>
    <div class="range range--curios"><h2 class="range__title">Curios</h2>
      <ul><li>Figurines</li><li>Brass Statues</li><li>Telescopes</li><li>Compasses</li><li>Gramophone</li><li>Hour Glasses</li><li>Sextants</li><li>Magnifying Lens</li><li>Prayer Wheels</li><li>Singing Bowls</li><li>Incense Holder</li><li>Trumpet</li></ul></div>
    <div class="range range--furniture"><h2 class="range__title">Furniture</h2>
      <ul><li>Cupboards</li><li>Tables</li><li>Stools</li><li>Chairs</li><li>Bookcases</li><li>Consoles</li><li>Cart</li><li>Trolley</li><li>Ceramic Knobs</li><li>Ladders</li><li>Umbrellas</li><li>Planters</li><li>Screen</li></ul></div>
    <div class="range range--decor"><h2 class="range__title">Decor</h2>
      <ul><li>Cushions</li><li>Photo-frames</li><li>Decorative Ornaments</li><li>Vases</li><li>Bowls</li><li>Clocks</li><li>Mirrors</li><li>Bird Cages</li><li>Sedge Mats</li><li>Glass Decanters</li><li>Pattachitra Bottles</li><li>Bird Cage Stands</li></ul></div>
    <div class="range range--misc"><h2 class="range__title">Miscellaneous</h2>
      <ul><li>Gift Bags</li><li>Wrapping Paper</li><li>Wine Bottle Holder</li><li>Xmas Decorations</li></ul></div>
    <div class="range range--fashion"><h2 class="range__title">Fashion</h2>
      <ul><li>Shawls / Scarves</li><li>Mufflers</li><li>Bags</li><li>Bangles</li><li>Flip-Flops</li></ul></div>
  </section>

</main>
</body>
</html>
```